"Copper Meadow" red wine label design

We are a Sydney based company. We need to design a wine label for a Australian red wine.
Front label include following info:
Our brand: "Copper Meadow";
Product name: "Shiraz 2016";
In the bottom with small font: "Wine of Australia", "750ml"
Back label:
the back label would need to be consistent with the front label, with space for one paragraph of tasting notes, and ingredient info etc.
we would like to use white, gold and blue in this label. It should make customer feel the magical and beautiful moment of starry night.

We also need a logo design for the wine brand: "Copper Meadow"

I have attached a few wine bottle that used blue to give you some inspirations.

We need the design in AI file format.

Target Market(s)

both men and women

Industry/Entity Type

It Company

Logo Text

Copper Meadow

Requirements
Nice to have
• gold borderline, words; use of blue and white

```html
<!DOCTYPE html>
<html lang="en">
<head>
<meta charset="utf-8">
<title>Copper Meadow Shiraz 2016 – Front Label</title>
<link rel="stylesheet" href="https://fonts.googleapis.com/css2?family=Great+Vibes&family=Cormorant+Garamond:wght@400;500&family=Arimo&display=swap">
<style>
  :root {
    --backdrop: #f5ecdc;
    --night-deep: #15193a;
    --night-mid: #262a5c;
    --night-violet: #3b1f5e;
    --night-plum: #4a1c5a;
    --silver-white: #eceef6;
    --soft-white: #d9dbe8;
    --gold: #c9a45a;
  }
  * { margin: 0; padding: 0; box-sizing: border-box; }
  html, body {
    width: 1200px;
    height: 862px;
    overflow: hidden;
    background: var(--backdrop);
  }
  .canvas {
    width: 1200px;
    height: 862px;
    display: flex;
    align-items: center;
    justify-content: center;
  }
  .front-label {
    position: relative;
    width: 440px;
    height: 640px;
    border-radius: 6px;
    overflow: hidden;
    color: var(--silver-white);
    text-align: center;
    box-shadow: 0 10px 30px rgba(60, 40, 20, 0.18);
  }
  .night-sky {
    position: absolute;
    inset: 0;
    background:
      radial-gradient(ellipse 60% 45% at 55% 38%, rgba(90, 100, 150, 0.35), transparent 70%),
      radial-gradient(ellipse 70% 40% at 20% 95%, var(--night-plum), transparent 70%),
      radial-gradient(ellipse 60% 50% at 85% 15%, var(--night-violet), transparent 70%),
      linear-gradient(175deg, var(--night-mid) 0%, var(--night-deep) 55%, var(--night-violet) 100%);
  }
  .label-content {
    position: relative;
    height: 100%;
  }
  .brand-mark {
    position: absolute;
    top: 38px;
    left: 0;
    right: 0;
    font-family: "Cormorant Garamond", serif;
    font-variant: small-caps;
    font-size: 19px;
    letter-spacing: 1px;
    color: var(--soft-white);
  }
  .wine-name {
    position: absolute;
    top: 210px;
    left: 0;
    right: 0;
    font-family: "Great Vibes", cursive;
    font-weight: 400;
    font-size: 64px;
    line-height: 66px;
    color: var(--silver-white);
  }
  .flourish {
    position: absolute;
    top: 402px;
    left: 50%;
    width: 44px;
    height: 14px;
    margin-left: -22px;
    border-radius: 7px;
    background: var(--gold);
    opacity: 0.55;
  }
  .varietal {
    position: absolute;
    top: 450px;
    left: 0;
    right: 0;
    font-family: "Cormorant Garamond", serif;
    font-weight: 500;
    color: var(--silver-white);
  }
  .varietal-grape {
    display: block;
    font-variant: small-caps;
    font-size: 30px;
    line-height: 30px;
    letter-spacing: 1px;
  }
  .varietal-vintage {
    display: block;
    font-size: 27px;
    line-height: 32px;
  }
  .legal-details {
    position: absolute;
    bottom: 44px;
    left: 0;
    right: 0;
    font-family: "Arimo", sans-serif;
    font-size: 11px;
    line-height: 18px;
    color: var(--soft-white);
  }
</style>
</head>
<body>
  <main class="canvas">
    <article class="front-label">
      <div class="night-sky" role="img" aria-label="Watercolour night sky in deep blue and violet with a faint milky way and scattered gold foil stars"></div>
      <div class="label-content">
        <p class="brand-mark">Copper Meadow</p>
        <h1 class="wine-name">Copper<br>Meadow</h1>
        <div class="flourish" role="img" aria-label="Small gold scroll flourish"></div>
        <p class="varietal">
          <span class="varietal-grape">Shiraz</span>
          <span class="varietal-vintage">2016</span>
        </p>
        <p class="legal-details">Wine of Australia<br>750ml&nbsp; 13,5% Alc.Vol.</p>
      </div>
    </article>
  </main>
</body>
</html>
```